Investment Management Firm Power point template

Harrowgate Capital is a real estate investment firm focused on buying commercial office and residential property in the UK. We produce powerpoint presentations for our Board of Directors, Investment Committee and also to external investors.

We are looking for a powerpoint design template which we can use for future presentations which provide a professional look and feel.

Our current website: http://www.harrowgatecapital.co.uk/

Target Market(s)

Institution Investors, Board of Directors, Professionals

Industry/Entity Type

Real Estate

Requirements
Must have
• Leverage off the current logo and colour scheme. However, does not have to purely rely on this colour scheme.
• - Title page
• - Content Page
• - Slide where graphs can be incorporated
• - Slide where photos can be incorporated
• - Slide of UK Map which can show where the property portfolio is currently located
• - Other slides incorporating smart art or other designs that can be used for future presentations
Nice to have
• An example of graphics that we would love to have in the powerpoint pack which we can easily edit has been attached

```html
<!DOCTYPE html>
<html lang="en">
<head>
<meta charset="utf-8">
<title>Project Slide – Image and Text</title>
<link href="https://fonts.googleapis.com/css2?family=Titillium+Web:wght@400;600;700&display=swap" rel="stylesheet">
<style>
  :root {
    --header-blue: #2f5673;
    --header-edge: #24465f;
    --footer-dark: #333333;
    --slide-bg: #f6f7f8;
    --caption-grey: #a9abad;
    --body-text: #4f5357;
    --white: #ffffff;
    --photo-top: #8a8fa3;
    --photo-mid: #a8998a;
    --photo-low: #6b6560;
  }
  * { margin: 0; padding: 0; box-sizing: border-box; }
  html, body { width: 1200px; height: 900px; overflow: hidden; }
  body {
    font-family: "Titillium Web", Arial, sans-serif;
    background: var(--slide-bg);
  }
  .slide {
    position: relative;
    width: 1200px;
    height: 900px;
    background: linear-gradient(180deg, #eef0f2 0%, var(--slide-bg) 30%, #ffffff 100%);
    overflow: hidden;
  }
  .slide-header {
    position: absolute;
    top: 0; left: 0;
    width: 100%;
    height: 90px;
    background: var(--header-blue);
    border-bottom: 2px solid var(--header-edge);
    display: flex;
    align-items: center;
    justify-content: space-between;
    padding: 0 40px 0 24px;
  }
  .project-title {
    color: var(--white);
    font-weight: 700;
    font-size: 42px;
    letter-spacing: 0.2px;
  }
  .brand {
    display: flex;
    align-items: center;
    gap: 10px;
    color: var(--white);
    font-weight: 600;
    font-size: 22px;
  }
  .brand-mark {
    width: 14px; height: 14px;
    border: 2px solid var(--white);
  }
  .image-caption {
    position: absolute;
    top: 198px; left: 0;
    width: 642px;
    height: 60px;
    background: var(--caption-grey);
    color: var(--white);
    font-weight: 600;
    font-size: 36px;
    text-align: right;
    padding-right: 20px;
    line-height: 60px;
  }
  .feature-photo {
    position: absolute;
    top: 264px; left: 0;
    width: 642px;
    height: 501px;
    background: linear-gradient(180deg, var(--photo-top) 0%, var(--photo-mid) 50%, var(--photo-low) 100%);
  }
  .body-copy {
    position: absolute;
    top: 193px; left: 668px;
    width: 452px;
    color: var(--body-text);
    font-size: 20.5px;
    letter-spacing: 0.2px;
    line-height: 30px;
  }
  .body-copy p + p { margin-top: 30px; }
  .slide-footer {
    position: absolute;
    bottom: 0; left: 0;
    width: 100%;
    height: 39px;
    background: var(--footer-dark);
  }
</style>
</head>
<body>
  <div class="slide">
    <header class="slide-header">
      <h1 class="project-title">Project Title Here</h1>
      <div class="brand"><span class="brand-mark"></span>Northmere Holdings</div>
    </header>

    <div class="image-caption">Image Title Here</div>
    <div class="feature-photo" role="img" aria-label="Feature photograph area"></div>

    <div class="body-copy">
      <p>Lorem ipsum dolor sit ipsum Lorem ipsum dolor sit ipsum Lorem ipsum dolor sit ipsum Lorem ipsum dolor sit ipsum Lorem ipsum dolor sit ipsum Lorem ipsum dolor sit ipsum</p>
      <p>Lorem ipsum dolor sit ipsum Lorem ipsum dolor sit ipsum Lorem ipsum dolor sit ipsum Lorem ipsum dolor sit ipsum Lorem ipsum dolor sit ipsum Lorem ipsum dolor sit ipsum Lorem ipsum dolor sit ipsum Lorem ipsum dolor sit ipsum Lorem ipsum dolor sit ipsum Lorem ipsum dolor sit ipsum</p>
      <p>Lorem ipsum dolor sit ipsum Lorem ipsum dolor sit ipsum Lorem ipsum dolor sit ipsum Lorem ipsum dolor sit ipsum</p>
      <p>Lorem ipsum dolor sit ipsum Lorem ipsum dolor sit ipsum Lorem ipsum dolor sit ipsum Lorem ipsum dolor sit ipsum</p>
    </div>

    <footer class="slide-footer"></footer>
  </div>
</body>
</html>
```